Gentlemen lifestyle blog in need of a logo and webdesign

Velmora is a site all about tests and reviews of products for gentlemen (Gin, whiskey, barber products, outdoor equipment, tobacco, coffe and more). It will be about fashion and a luxury lifestyle, health and fitness.
it will also include a online store

```html
<!DOCTYPE html>
<html lang="en">
<head>
<meta charset="utf-8">
<title>Velmora – The Modern Gentleman</title>
<link href="https://fonts.googleapis.com/css2?family=Russo+One&family=Roboto:wght@400;500;700&display=swap" rel="stylesheet">
<style>
:root{
  --black:#000;
  --panel:#111;
  --card:#141414;
  --orange:#f7a600;
  --white:#fff;
  --muted:#b5b5b5;
  --line:#2a2a2a;
}
*{box-sizing:border-box;margin:0;padding:0}
html,body{width:1200px;height:3638px;overflow:hidden;background:var(--black);color:var(--white);font-family:"Roboto",sans-serif}
.page{position:relative;width:1200px;height:3638px}
.abs{position:absolute}
.photo{display:block}

.topbar{top:0;left:0;width:1200px;height:89px;background:var(--black)}
.logo{left:111px;top:30px;font-weight:700;font-size:21px;letter-spacing:.5px}
.search{left:426px;top:26px;width:254px;height:37px;border-radius:19px;background:#fff;color:#999;font-size:12px;padding:11px 16px}
.search svg{position:absolute;right:14px;top:11px}
.hbtn{top:26px;display:flex;align-items:center;gap:10px;font-weight:700;font-size:15px}
.hbtn .dot{width:36px;height:36px;border-radius:50%;background:var(--orange);display:flex;align-items:center;justify-content:center}
.social-top{left:960px;top:26px;display:flex;gap:10px}
.ring{width:36px;height:36px;border-radius:50%;border:1.5px solid #fff}
.nav{top:89px;left:0;width:1200px;height:45px;background:var(--orange);display:flex;padding-left:108px;align-items:center}
.nav a{color:#111;text-decoration:none;font-size:15px;font-weight:500;margin-right:24px}

.hero{top:134px;left:0;width:1200px;height:569px;background:linear-gradient(90deg,#2a1c12 0%,#3d2a1a 35%,#1e1612 60%,#3a2418 100%)}
.hero h1{position:absolute;left:111px;top:182px;font-family:"Russo One",sans-serif;font-size:39px;line-height:52px;font-weight:400;text-transform:uppercase}
.hero p{position:absolute;left:111px;top:352px;font-weight:500;font-size:17px}

.sec-title{font-family:"Russo One",sans-serif;font-size:28px;text-transform:uppercase;font-weight:400}
.sec-title span{color:var(--orange)}

.tile{display:flex;align-items:flex-end;justify-content:center;padding-bottom:22px;font-weight:700;font-size:18px;text-shadow:0 1px 3px #000}

.post{left:111px;width:598px;height:209px;background:var(--card)}
.post .photo{position:absolute;left:9px;top:9px;width:177px;height:191px}
.post .body{position:absolute;left:223px;top:36px;width:350px}
.meta{display:flex;align-items:center;gap:18px;font-size:11px;font-weight:500}
.tag{background:var(--orange);padding:2px 10px;font-weight:700;font-size:12px}
.post h3{font-size:17px;font-weight:700;margin:16px 0 12px}
.post p{font-size:13px;color:var(--muted);line-height:21px}
.more{margin-top:14px;color:var(--orange);font-weight:700;font-size:13px;display:flex;align-items:center;gap:6px}

.side{left:755px;width:334px;background:var(--panel)}
.side-head{position:absolute;left:9px;top:12px;width:316px;height:39px;background:var(--orange);font-family:"Russo One",sans-serif;text-transform:uppercase;display:flex;align-items:center;justify-content:center;font-size:16px}
.mini{position:absolute;left:23px;width:290px;height:96px}
.mini .photo{position:absolute;left:0;top:0;width:120px;height:96px}
.mini h4{position:absolute;left:136px;top:10px;width:160px;font-size:14px;font-weight:700;line-height:20px}
.mini .date{position:absolute;left:136px;top:69px;font-size:13px;color:#ddd;display:flex;gap:6px;align-items:center}
.cat{position:absolute;left:25px;font-size:15px;display:flex;gap:18px;align-items:center}
.quote{position:absolute;left:13px;width:310px;display:flex;gap:16px}
.quote .av{width:72px;height:72px;border-radius:50%;flex:none}
.quote p{font-size:13px;color:#ddd;line-height:19px}
.quote b{display:block;font-size:13px;margin-top:9px}

.cm{width:284px;height:368px;background:var(--card)}
.cm .photo{width:284px;height:171px}
.cm .in{padding:22px 16px 0}
.cm small{font-size:11px;font-weight:500}
.cm h3{font-size:15px;font-weight:700;line-height:22px;margin:8px 0 10px}
.cm p{font-size:13px;color:var(--muted);line-height:22px}
.cm .foot{position:absolute;bottom:0;left:0;width:284px;height:46px;border-top:1px solid var(--line);display:flex;align-items:center;justify-content:center;gap:14px;font-size:13px}

.news{top:3153px;left:0;width:1200px;height:176px;background:linear-gradient(90deg,#1a2024,#2c363b 50%,#1a2226)}
.news small{position:absolute;left:111px;top:58px;font-size:13px;font-weight:500}
.news h2{position:absolute;left:111px;top:82px;font-family:"Russo One",sans-serif;font-size:28px;font-weight:400;text-transform:uppercase}
.email{position:absolute;left:584px;top:68px;width:307px;height:48px;border-radius:24px;background:#fff;color:#999;font-size:12px;display:flex;align-items:center;gap:8px;padding-left:20px}
.submit{position:absolute;left:911px;top:68px;width:142px;height:48px;border-radius:24px;background:var(--orange);font-weight:700;font-size:15px;display:flex;align-items:center;justify-content:center}

.flogo{top:3413px;left:0;width:1200px;text-align:center;font-weight:700;font-size:24px}
.flinks{top:3478px;left:0;width:1200px;display:flex;justify-content:center;gap:14px;font-size:16px}
.flinks i{font-style:normal;color:#aaa}
.contact{left:111px;font-size:14px;display:flex;gap:20px;align-items:center}
.fsocial{left:469px;top:3554px;display:flex;gap:14px}
.fsocial .ring{width:42px;height:42px}
.copy{right:112px;text-align:right;font-size:14px}
</style>
</head>
<body>
<div class="page">

  <header class="abs topbar">
    <div class="abs logo">VELMORA</div>
    <div class="abs search">Search
      <svg width="16" height="16" viewBox="0 0 16 16"><circle cx="6.5" cy="6.5" r="5" fill="none" stroke="#111" stroke-width="2"/><path d="M10.5 10.5l4 4" stroke="#111" stroke-width="2"/></svg>
    </div>
    <div class="abs hbtn" style="left:720px">
      <span class="dot"><svg width="14" height="14" viewBox="0 0 14 14"><circle cx="7" cy="4" r="3" fill="#111"/><path d="M1 14c0-4 3-6 6-6s6 2 6 6z" fill="#111"/></svg></span>LOGIN
    </div>
    <div class="abs hbtn" style="left:839px">
      <span class="dot"><svg width="16" height="14" viewBox="0 0 16 14"><path d="M0 1h3l2 8h9l2-6H4" fill="none" stroke="#111" stroke-width="2"/><circle cx="6" cy="12" r="1.5" fill="#111"/><circle cx="13" cy="12" r="1.5" fill="#111"/></svg></span>CART
    </div>
    <div class="abs social-top" aria-label="Social links">
      <span class="ring"></span><span class="ring"></span><span class="ring"></span>
    </div>
  </header>

  <nav class="abs nav">
    <a>Home</a><a>Luxury Lifestyle</a><a>Health &amp; Fitness</a><a>Fashion</a><a>Gin</a><a>Whiskey</a><a>Barber</a><a>Reviews</a><a>Tobacco</a><a>Store</a><a>Events</a><a>Contact Us</a>
  </nav>

  <section class="abs hero" role="img" aria-label="Gentleman in a suit tasting red wine in front of a wine cellar">
    <h1>Elevate your lifestyle -<br>the ultimate guide for<br>the modern gentleman</h1>
    <p>Expert Reviews | Timeless Style | Premium Craftsmanship</p>
  </section>

  <h2 class="abs sec-title" style="left:111px;top:786px">Featured <span>Products</span></h2>
  <div class="abs tile" style="left:111px;top:854px;width:303px;height:195px;background:linear-gradient(135deg,#6a4322,#2e1c10)" role="img" aria-label="Barber shop with leather chair and grooming tools">Barber &amp; Grooming</div>
  <div class="abs tile" style="left:111px;top:1066px;width:303px;height:194px;background:linear-gradient(135deg,#3a3d35,#1a1c1a)" role="img" aria-label="Gin glass with limes">Gin</div>
  <div class="abs tile" style="left:428px;top:854px;width:344px;height:406px;background:linear-gradient(180deg,#4a2a12,#7a4a1a 60%,#2a180c)" role="img" aria-label="Row of whiskey tasting glasses on a bar">Whiskey &amp; Spirits</div>
  <div class="abs tile" style="left:786px;top:854px;width:303px;height:195px;background:linear-gradient(135deg,#a5753f,#4e3218)" role="img" aria-label="Cigars on a wooden table">Cigars &amp; Tobacco</div>
  <div class="abs tile" style="left:786px;top:1066px;width:303px;height:194px;background:linear-gradient(135deg,#2a2420,#5a3e28)" role="img" aria-label="Coffee cup with heart-shaped steam">Coffee &amp; Lifestyle</div>

  <h2 class="abs sec-title" style="left:111px;top:1338px">Recent <span>Update</span></h2>

  <article class="abs post" style="top:1426px">
    <div class="photo abs" style="background:linear-gradient(135deg,#5a5f63,#2d3033)" role="img" aria-label="Man in a suit reading a magazine on a sofa"></div>
    <div class="body">
      <div class="meta"><span class="tag">News</span><span>By John Doe</span><span>Feb 6, 2025</span></div>
      <h3>Sed ut perspiciatis unde omnis iste natus</h3>
      <p>Lorem ipsum dolor sit amet, consectetur adipiscing elit, sed do eiusmod tempor incididunt ut labore et</p>
      <div class="more">READ MORE <svg width="12" height="12"><circle cx="6" cy="6" r="6" fill="#f7a600"/><path d="M5 3l3 3-3 3" stroke="#111" stroke-width="1.6" fill="none"/></svg></div>
    </div>
  </article>
  <article class="abs post" style="top:1662px">
    <div class="photo abs" style="background:linear-gradient(135deg,#d8d4cd,#9a7a58)" role="img" aria-label="Man in sunglasses wearing a camel coat"></div>
    <div class="body">
      <div class="meta"><span class="tag">News</span><span>By John Doe</span><span>Feb 6, 2025</span></div>
      <h3>Sed ut perspiciatis unde omnis iste natus</h3>
      <p>Lorem ipsum dolor sit amet, consectetur adipiscing elit, sed do eiusmod tempor incididunt ut labore et</p>
      <div class="more">READ MORE <svg width="12" height="12"><circle cx="6" cy="6" r="6" fill="#f7a600"/><path d="M5 3l3 3-3 3" stroke="#111" stroke-width="1.6" fill="none"/></svg></div>
    </div>
  </article>
  <article class="abs post" style="top:1898px">
    <div class="photo abs" style="background:linear-gradient(135deg,#cfd2cf,#3a8fb5)" role="img" aria-label="Man doing a plank on a blue yoga mat"></div>
    <div class="body">
      <div class="meta"><span class="tag">News</span><span>By John Doe</span><span>Feb 6, 2025</span></div>
      <h3>Sed ut perspiciatis unde omnis iste natus</h3>
      <p>Lorem ipsum dolor sit amet, consectetur adipiscing elit, sed do eiusmod tempor incididunt ut labore et</p>
      <div class="more">READ MORE <svg width="12" height="12"><circle cx="6" cy="6" r="6" fill="#f7a600"/><path d="M5 3l3 3-3 3" stroke="#111" stroke-width="1.6" fill="none"/></svg></div>
    </div>
  </article>

  <aside class="abs side" style="top:1338px;height:427px">
    <div class="side-head">Recent Stories</div>
    <div class="mini" style="top:79px"><div class="photo" style="background:linear-gradient(135deg,#7d8a95,#3a4550)" role="img" aria-label="Runner in a city"></div><h4>Sed perspiciatis unde omnis iste natus</h4><div class="date"><svg width="12" height="12"><rect x="1" y="2" width="10" height="9" fill="#f7a600"/></svg>Apr 06, 2025</div></div>
    <div class="mini" style="top:188px"><div class="photo" style="background:linear-gradient(135deg,#8a8060,#3e3a2a)" role="img" aria-label="Tent by a lake with campfire"></div><h4>Sed perspiciatis unde omnis iste natus</h4><div class="date"><svg width="12" height="12"><rect x="1" y="2" width="10" height="9" fill="#f7a600"/></svg>Apr 06, 2025</div></div>
    <div class="mini" style="top:295px"><div class="photo" style="background:linear-gradient(135deg,#c07a2a,#3a1e0a)" role="img" aria-label="Whiskey being poured"></div><h4>Sed perspiciatis unde omnis iste natus</h4><div class="date"><svg width="12" height="12"><rect x="1" y="2" width="10" height="9" fill="#f7a600"/></svg>Apr 06, 2025</div></div>
  </aside>

  <aside class="abs side" style="top:1810px;height:425px">
    <div class="side-head">Latest Articles</div>
    <div class="mini" style="top:77px"><div class="photo" style="background:linear-gradient(135deg,#6a5848,#2a2018)" role="img" aria-label="Barbers in a shop"></div><h4>Sed perspiciatis unde omnis iste natus</h4><div class="date"><svg width="12" height="12"><rect x="1" y="2" width="10" height="9" fill="#f7a600"/></svg>Apr 06, 2025</div></div>
    <div class="mini" style="top:186px"><div class="photo" style="background:linear-gradient(135deg,#3a3f48,#14161a)" role="img" aria-label="Man smoking a cigar"></div><h4>Sed perspiciatis unde omnis iste natus</h4><div class="date"><svg width="12" height="12"><rect x="1" y="2" width="10" height="9" fill="#f7a600"/></svg>Apr 06, 2025</div></div>
    <div class="mini" style="top:293px"><div class="photo" style="background:linear-gradient(135deg,#6e8a62,#c8642a)" role="img" aria-label="Orange tent in the mountains"></div><h4>Sed perspiciatis unde omnis iste natus</h4><div class="date"><svg width="12" height="12"><rect x="1" y="2" width="10" height="9" fill="#f7a600"/></svg>Apr 06, 2025</div></div>
  </aside>

  <aside class="abs side" style="top:2284px;height:286px">
    <div class="side-head">All Categories</div>
    <div class="cat" style="top:92px"><svg width="10" height="10"><path d="M1 1l3 4-3 4M5 1l3 4-3 4" stroke="#f7a600" fill="none" stroke-width="1.4"/></svg>Whiskey &amp; Spirits</div>
    <div class="cat" style="top:129px"><svg width="10" height="10"><path d="M1 1l3 4-3 4M5 1l3 4-3 4" stroke="#f7a600" fill="none" stroke-width="1.4"/></svg>Barber &amp; Grooming</div>
    <div class="cat" style="top:166px"><svg width="10" height="10"><path d="M1 1l3 4-3 4M5 1l3 4-3 4" stroke="#f7a600" fill="none" stroke-width="1.4"/></svg>Watches &amp; Accessories</div>
    <div class="cat" style="top:203px"><svg width="10" height="10"><path d="M1 1l3 4-3 4M5 1l3 4-3 4" stroke="#f7a600" fill="none" stroke-width="1.4"/></svg>Cigars &amp; Tobacco</div>
    <div class="cat" style="top:240px"><svg width="10" height="10"><path d="M1 1l3 4-3 4M5 1l3 4-3 4" stroke="#f7a600" fill="none" stroke-width="1.4"/></svg>Outdoor &amp; Adventure</div>
  </aside>

  <aside class="abs side" style="top:2619px;height:424px">
    <div class="side-head">Customers Say</div>
    <div class="quote" style="top:80px"><div class="av" style="background:#556070" role="img" aria-label="Customer portrait"></div><div><p>“Velmora is my go-to for whiskey recommendations. Their taste is impeccable!”</p><b>James R.</b></div></div>
    <div class="quote" style="top:199px"><div class="av" style="background:#6a4a38" role="img" aria-label="Customer portrait"></div><div><p>“I never knew grooming could be this refined until I found this blog!”</p><b>Mark T.</b></div></div>
    <div class="quote" style="top:307px"><div class="av" style="background:#40505e" role="img" aria-label="Customer portrait"></div><div><p>“Bought a watch from the Velmora store, and it’s perfect!”</p><b>Daniel K.</b></div></div>
  </aside>

  <h2 class="abs sec-title" style="left:111px;top:2186px">Recent <span>Comments</span></h2>

  <article class="abs cm" style="left:111px;top:2268px">
    <div class="photo" style="background:linear-gradient(135deg,#2e3a2a,#c98a3a)" role="img" aria-label="Tent and campfire in a forest"></div>
    <div class="in"><small>ON TRAVEL</small><h3>Lorem ipsum dolor sit consectetur adipiscing elit, sed</h3><p>Sed ut perspiciatis unde omnis iste natus error sit voluptatem</p></div>
    <div class="foot"><span style="color:#f7a600">●</span>John Doe <span>|</span><span style="color:#f7a600">▪</span>Mar 11, 2025</div>
  </article>
  <article class="abs cm" style="left:425px;top:2268px">
    <div class="photo" style="background:linear-gradient(135deg,#a89a8a,#3a3430)" role="img" aria-label="Man in leather jacket sitting on steps"></div>
    <div class="in"><small>ON TRAVEL</small><h3>Lorem ipsum dolor sit consectetur adipiscing elit, sed</h3><p>Sed ut perspiciatis unde omnis iste natus error sit voluptatem</p></div>
    <div class="foot"><span style="color:#f7a600">●</span>John Doe <span>|</span><span style="color:#f7a600">▪</span>Mar 11, 2025</div>
  </article>
  <article class="abs cm" style="left:111px;top:2673px">
    <div class="photo" style="background:linear-gradient(135deg,#1c2430,#6a2218)" role="img" aria-label="Man in suit smoking in a leather armchair"></div>
    <div class="in"><small>ON TRAVEL</small><h3>Lorem ipsum dolor sit consectetur adipiscing elit, sed</h3><p>Sed ut perspiciatis unde omnis iste natus error sit voluptatem</p></div>
    <div class="foot"><span style="color:#f7a600">●</span>John Doe <span>|</span><span style="color:#f7a600">▪</span>Mar 11, 2025</div>
  </article>
  <article class="abs cm" style="left:425px;top:2673px">
    <div class="photo" style="background:linear-gradient(135deg,#e8e8dc,#6a8a3a)" role="img" aria-label="Gin and tonic with lime"></div>
    <div class="in"><small>ON TRAVEL</small><h3>Lorem ipsum dolor sit consectetur adipiscing elit, sed</h3><p>Sed ut perspiciatis unde omnis iste natus error sit voluptatem</p></div>
    <div class="foot"><span style="color:#f7a600">●</span>John Doe <span>|</span><span style="color:#f7a600">▪</span>Mar 11, 2025</div>
  </article>

  <section class="abs news" role="img" aria-label="Smoky dark background">
    <small>Subscribe Our newsletter to get latest updates</small>
    <h2>Sign up to our newsletter</h2>
    <div class="email"><svg width="12" height="9"><rect x=".5" y=".5" width="11" height="8" fill="#999"/></svg>Your Email Address</div>
    <div class="submit">SUBMIT</div>
  </section>

  <footer>
    <div class="abs flogo">VELMORA</div>
    <div class="abs flinks"><span>Home</span><i>|</i><span>About</span><i>|</i><span>Newsletter</span><i>|</i><span>Features</span><i>|</i><span>Topics</span><i>|</i><span>Contact Us</span><i>|</i><span>Terms &amp; Conditions</span><i>|</i><span>FAQs</span></div>
    <div class="abs contact" style="top:3545px"><svg width="18" height="18" viewBox="0 0 18 18"><path d="M4 1l3 4-2 2c1 3 3 5 6 6l2-2 4 3-2 3C8 17 1 10 1 3z" fill="none" stroke="#f7a600" stroke-width="1.4"/></svg>(555) 014-2290</div>
    <div class="abs contact" style="top:3586px"><svg width="20" height="14" viewBox="0 0 20 14"><rect x="1" y="1" width="18" height="12" fill="none" stroke="#f7a600" stroke-width="1.4"/><path d="M1 1l9 7 9-7" fill="none" stroke="#f7a600" stroke-width="1.4"/></svg>info@velmora.com</div>
    <div class="abs fsocial" aria-label="Social links"><span class="ring"></span><span class="ring"></span><span class="ring"></span><span class="ring"></span><span class="ring"></span></div>
    <div class="abs copy" style="top:3546px">© Copyright 2025 Velmora.</div>
    <div class="abs copy" style="top:3581px">All Rights Reserved</div>
  </footer>

</div>
</body>
</html>
```